3 -4 PAGE GIFT CERTIFICATE REDEMPTION WEBSITE REVAMP

I am revamping the entire website at www.brightperksportal.net

Will have brand new theme and new logo. Name Of Company:
Bounty Motivation Delivery Networks
BMDN

OVERVIEW:
I NEED A 3-4 PAGE WEBSITE DESIGNED WITH CHECKOUT MODULE.
My company offers fully brandable and personalizable gift certificates good for travel, vacations, dining rewards, rebates, electronic gifts, etc. and I need to redesign the website where the fulfillment and redemption happens.

So the way it works is a business uses my online platform to create, brand and personalize these gift certificates. The business can brand the certificates in the upper right hand corner of each certificate where the “Compliments Of” area sits with their company logo, website, contact info, etc and can also personalize each individual gift certificate to a specific customer too. SEE EXAMPLE ATTACHED TO BRIEF.

The example I attached to this brief includes a logo which is really just a picture and under it there is 3 lines of text where the business can put a website, phone number and email.

On the left side of the top banner image you will see “Exclusively For”.

So now, after a customer enters their certificate ID #, the branding on the next page must match the Compliments Of area and also must personalize the Sales Page to the customer that is in the Exclusively For” area of the certificate…...

Page 1: LANDING PAGE
CONTENT:

Welcome to the online redemption source for vacation certificates, travel vouchers, digital electronic products, dining incentives, gas and grocery rewards and more!

ENTER YOUR CERTIFICATE ID #
ENTER YOUR EMAIL

Welcome to the online redemption system for vacation certificates, travel vouchers, rebates, digital products, dining incentives, gas and grocery rewards and more!

PLEASE ENTER A VALID CERTIFICATE ID NUMBER TO VIEW THE DETAILS AND TO REDEEM AND ACTIVATE YOUR SPECIAL OFFER.

Also we need a testimonial module ON THIS PAGE AND SALES PAGE

PAGE 2: SALES PAGE FOR OFFER (we will use the 1-4 Night Las Vegas Hotel Stay Certificate)
INSTRUCTIONS EXPLANATION FOR DESIGNER: Every gift certificate has a "Compliments Of Area" in the upper right hand corner....SEE SAMPLE ATTACHED TO BRIEF. On the sales page we also show this to the customer after they enter the code. Every certificate has a Compliments Of area and we will also add "Exclusively For" so the person that is giving the certificate away can specify the name of the recipient so we will also transffer this information over to the SALES PAGE.

CONTENT FOR SALES PAGE:

WELCOME ~~NAME OF PERSON IN EXCLUSIVELY FOR AREA ON CERTIFICATE~~ !!

THIS SPECIAL INCENTIVE OFFER IS COMPLIMENTS OF

~~LOGO THAT IS SEEN ON CERTIFICATE~~
~~TEXT LINE 1~~
~~TEXT LINE 2~~
~~TEXT LINE 3~~

TITLE OF OFFER: STAY & PLAY IN LAS VEGAS FOR UP TO 4 NIGHTS!
There is no doubt that Las Vegas is one of the hottest travel destinations around the world. In fact, some people would even go as far as saying that perhaps it is THE hottest place to visit. Enjoy up to 4 nights of resort/casino accommodations in exciting Las Vegas, NV. Millions of people travel to this exciting city each year to enjoy its thrills. Thanks to the business you received this certificate from, now you can enjoy Las Vegas, NV too!

Features:
*Travel 7 Days A Week
*Stay Your Choice Of Nights (1-4 Nights)
*Good For Two Adults & Two Children
*Pay Just The Taxes & Fees
*Multiple Travel Date Requests Allowed
*Fully Transferable To Another Person
*Just A 30 Days Advance Notice Required
*You Will Have 12 Months To Complete Travel

HOW CAN WE DO THIS?

We contract with the world leading hotel chains and resorts to help them fill their otherwise empty rooms.

We help fill empty rooms which the hotels, resorts and cruise lines turn into additional revenue from other areas of their property and future bookings.

Hotels rarely experience full occupancy, yet they remain open, providing rooms and services at fixed costs. So when hotels give out their rooms by partnering with marketing companies like us, they might miss out on the room fee, but they already didn't have that in the first place, at least now they have the opportunity to gain a customer for their in-house restaurants, room service, their casinos, an extra day stay, future bookings, etc.

The magic of why our program works so well is the fact that it’s a win win for everyone involved. You win because you received a huge savings. The business who gave you the certificate wins because now you will remember them the next time you need the same kind of product or service that they provide and you might even refer your friends and family members. The hotels and resorts win because they gain additional revenue from other areas of their establishment that they otherwise would not have been able to get and they also have a new client that may book with them in the future. Remember, they didn’t have anyone in the room in the first place so since you are paying the normal rack rate you might be more inclined to spend your money at the hotel. You are never under any obligation to do so though!

Retail Value: Up to $826.00 (based on $159.00 per night)

How it Works:
You will receive up to 4 nights in a 3 star or better Las Vegas resort and casino for up to 4 travelers, 2 adults and 2 children.

Simply redeem the certificate to activate the travel period for 1 year. This means you will have at least 1 year to travel from the date you redeem and activate your offer. Be sure to redeem your certificate before it expires! All certificates will have an accompanying expiration date attached to them.

When you are ready to book you will simply have to pay the daily room rate taxes and fees of approximately $12-$33 per night (not per person). On average the taxes and fees come out to about $19 per night. (Retail Value: Up to $826.00 based on $159.00 per night)

Step 1: Redeem your certificate to activate your offer

Step 2: Fill out the online reservation request form with travel dates within the next 12 months.

Step 3: Wait for a confirmation of your booked reservation. You will be notified immediately upon us booking your reservation.

Go on your vacation and thank the business who gave you this special offer by doing business with them again and referring your friends and family members!

No timeshares or sales presentations, Guaranteed!

PAGE 3 IS CHECKOUT PAGE:

PLEASE USE ****HERE IS SAMPLE CODE FOR YOU TO TEST OUT AT CURRENT REDEMPTION PROCESS WWW.BRIGHTPERKSPORTAL.NET 46205-17938

TO SEE THE CURRENT CHECK OUT. I NEED ALL THE SAME CONTENT JUST A DIFFERENT MORE EFFICIENT CHECKOUT PROCESS HERE. OMIT THE LEFT SIDE OF THE CURRENT CHECK OUT PROCESS AS THIS CURRENT PROCESSS IS ONE STEP AND DOES NOT HAVE A SALES PAGE BUT NOW I AM CREATING A SALES PAGE BEFORE THE CHECKOUT SO THE BRANDING AND PERSONALIZATION WILL HAPPEN ON THE SALES PAGE….THANK YOU

Target Market(s)

END USERS THAT ARE REDEEMING SPECIAL OFFERS GIFT CERTIFICATES

Industry/Entity Type

Marketing

Number of Pages Required

4 page

Colors

Designer to choose colors to be used in the design.

Requirements
Must have
• OVERVIEW:
• I NEED A 3-4 PAGE WEBSITE DESIGNED WITH CHECKOUT MODULE.
• My company offers fully brandable and personalizable gift certificates good for travel, vacations, dining rewards, rebates, electronic gifts, etc. and I need to redesign the website where the fulfillment and redemption happens.
• So the way it works is a business uses my online platform to create, brand and personalize these gift certificates. The business can brand the certificates in the upper right hand corner of each certificate where the “Compliments Of” area sits with their company logo, website, contact info, etc and can also personalize each individual gift certificate to a specific customer too. SEE EXAMPLE ATTACHED TO BRIEF.
• The example I attached to this brief includes a logo which is really just a picture and under it there is 3 lines of text where the business can put a website, phone number and email.
• On the left side of the top banner image you will see “Exclusively For”.
• So now, after a customer enters their certificate ID #, the branding on the next page must match the Compliments Of area and also must personalize the Sales Page to the customer that is in the Exclusively For” area of the certificate…...
• Page 1: LANDING PAGE
• CONTENT:
• Welcome to the online redemption source for vacation certificates, travel vouchers, digital electronic products, dining incentives, gas and grocery rewards and more!
• ENTER YOUR CERTIFICATE ID #
• ENTER YOUR EMAIL
• Welcome to the online redemption system for vacation certificates, travel vouchers, rebates, digital products, dining incentives, gas and grocery rewards and more!
• PLEASE ENTER A VALID CERTIFICATE ID NUMBER TO VIEW THE DETAILS AND TO REDEEM AND ACTIVATE YOUR SPECIAL OFFER.
• Also we need a testimonial module ON THIS PAGE AND SALES PAGE
• PAGE 2: SALES PAGE FOR OFFER (we will use the 1-4 Night Las Vegas Hotel Stay Certificate)
• INSTRUCTIONS EXPLANATION FOR DESIGNER: Every gift certificate has a "Compliments Of Area" in the upper right hand corner....SEE SAMPLE ATTACHED TO BRIEF. On the sales page we also show this to the customer after they enter the code. Every certificate has a Compliments Of area and we will also add "Exclusively For" so the person that is giving the certificate away can specify the name of the recipient so we will also transffer this information over to the SALES PAGE.
• CONTENT FOR SALES PAGE:
• WELCOME ~~NAME OF PERSON IN EXCLUSIVELY FOR AREA ON CERTIFICATE~~ !!
• THIS SPECIAL INCENTIVE OFFER IS COMPLIMENTS OF
• ~~LOGO THAT IS SEEN ON CERTIFICATE~~
• ~~TEXT LINE 1~~
• ~~TEXT LINE 2~~
• ~~TEXT LINE 3~~
• TITLE OF OFFER: STAY & PLAY IN LAS VEGAS FOR UP TO 4 NIGHTS!
• There is no doubt that Las Vegas is one of the hottest travel destinations around the world. In fact, some people would even go as far as saying that perhaps it is THE hottest place to visit. Enjoy up to 4 nights of resort/casino accommodations in exciting Las Vegas, NV. Millions of people travel to this exciting city each year to enjoy its thrills. Thanks to the business you received this certificate from, now you can enjoy Las Vegas, NV too!
• Features:
• *Travel 7 Days A Week
• *Stay Your Choice Of Nights (1-4 Nights)
• *Good For Two Adults & Two Children
• *Pay Just The Taxes & Fees
• *Multiple Travel Date Requests Allowed
• *Fully Transferable To Another Person
• *Just A 30 Days Advance Notice Required
• *You Will Have 12 Months To Complete Travel
• HOW CAN WE DO THIS?
• We contract with the world leading hotel chains and resorts to help them fill their otherwise empty rooms.
• We help fill empty rooms which the hotels, resorts and cruise lines turn into additional revenue from other areas of their property and future bookings.
• Hotels rarely experience full occupancy, yet they remain open, providing rooms and services at fixed costs. So when hotels give out their rooms by partnering with marketing companies like us, they might miss out on the room fee, but they already didn't have that in the first place, at least now they have the opportunity to gain a customer for their in-house restaurants, room service, their casinos, an extra day stay, future bookings, etc.
• The magic of why our program works so well is the fact that it’s a win win for everyone involved. You win because you received a huge savings. The business who gave you the certificate wins because now you will remember them the next time you need the same kind of product or service that they provide and you might even refer your friends and family members. The hotels and resorts win because they gain additional revenue from other areas of their establishment that they otherwise would not have been able to get and they also have a new client that may book with them in the future. Remember, they didn’t have anyone in the room in the first place so since you are paying the normal rack rate you might be more inclined to spend your money at the hotel. You are never under any obligation to do so though!
• Retail Value: Up to $826.00 (based on $159.00 per night)
• How it Works:
• You will receive up to 4 nights in a 3 star or better Las Vegas resort and casino for up to 4 travelers, 2 adults and 2 children.
• Simply redeem the certificate to activate the travel period for 1 year. This means you will have at least 1 year to travel from the date you redeem and activate your offer. Be sure to redeem your certificate before it expires! All certificates will have an accompanying expiration date attached to them.
• When you are ready to book you will simply have to pay the daily room rate taxes and fees of approximately $12-$33 per night (not per person). On average the taxes and fees come out to about $19 per night. (Retail Value: Up to $826.00 based on $159.00 per night)
• Step 1: Redeem your certificate to activate your offer
• Step 2: Fill out the online reservation request form with travel dates within the next 12 months.
• Step 3: Wait for a confirmation of your booked reservation. You will be notified immediately upon us booking your reservation.
• Go on your vacation and thank the business who gave you this special offer by doing business with them again and referring your friends and family members!
• No timeshares or sales presentations, Guaranteed!
• PAGE 3 IS CHECKOUT PAGE:
• PLEASE USE ****HERE IS SAMPLE CODE FOR YOU TO TEST OUT AT CURRENT REDEMPTION PROCESS WWW.BRIGHTPERKSPORTAL.NET 46205-17938
• TO SEE THE CURRENT CHECK OUT. I NEED ALL THE SAME CONTENT JUST A DIFFERENT MORE EFFICIENT CHECKOUT PROCESS HERE. OMIT THE LEFT SIDE OF THE CURRENT CHECK OUT PROCESS AS THIS CURRENT PROCESSS IS ONE STEP AND DOES NOT HAVE A SALES PAGE BUT NOW I AM CREATING A SALES PAGE BEFORE THE CHECKOUT SO THE BRANDING AND PERSONALIZATION WILL HAPPEN ON THE SALES PAGE….THANK YOU
Nice to have
• OVERVIEW:
• Page 1: LANDING PAGE
• CONTENT:
• ENTER YOUR EMAIL
• CONTENT FOR SALES PAGE:
• ~~TEXT LINE 1~~
• ~~TEXT LINE 2~~
• ~~TEXT LINE 3~~
• Features:
• *Travel 7 Days A Week
• HOW CAN WE DO THIS?
• How it Works:
Should not have
• OVERVIEW:
• Page 1: LANDING PAGE
• CONTENT:
• ENTER YOUR EMAIL
• CONTENT FOR SALES PAGE:
• ~~TEXT LINE 1~~
• ~~TEXT LINE 2~~
• ~~TEXT LINE 3~~
• Features:
• *Travel 7 Days A Week
• HOW CAN WE DO THIS?
• How it Works:

```html
<!DOCTYPE html>
<html lang="en">
<head>
<meta charset="utf-8">
<title>BrightPerksPortal – Redemption Source</title>
<link href="https://fonts.googleapis.com/css2?family=Roboto:wght@300;400;500;700;900&family=Poppins:wght@400;800&display=swap" rel="stylesheet">
<style>
  :root{
    --navy:#2d3a7c;
    --navy-deep:#3a2f6e;
    --sea:#3f5d9c;
    --orange:#f26b1d;
    --teal:#5ec3cf;
    --ink:#333333;
    --text:#6b6b6b;
    --field:#f6f6f6;
    --line:#dddddd;
    --band:#e8dedb;
    --footer:#eeeeee;
    --white:#ffffff;
  }
  *{margin:0;padding:0;box-sizing:border-box}
  html,body{width:853px;height:1200px;overflow:hidden;background:var(--white)}
  body{position:relative;font-family:'Roboto',sans-serif;color:var(--ink)}
  .abs{position:absolute}

  /* hero */
  .hero-bg{left:0;top:0;width:853px;height:420px}
  .brand{left:104px;top:38px}
  .brand-name{font-family:'Roboto',sans-serif;font-weight:900;font-size:19px;color:var(--orange);display:flex;align-items:center;gap:6px}
  .brand-dot{width:10px;height:10px;border-radius:50%;background:#f2b233}
  .brand-tag{font-size:6.5px;color:#e8e8f4;margin:3px 0 0 22px;letter-spacing:.2px}
  .nav{top:45px;display:flex;font-size:11.4px;font-weight:500;color:var(--white)}
  .nav a{color:var(--white);text-decoration:none;position:absolute;white-space:nowrap}
  .hero-title{left:105px;top:143px;font-size:27px;font-weight:700;line-height:33px;color:var(--white)}
  .hero-text{left:105px;top:222px;font-size:9.7px;line-height:17px;color:var(--white);width:320px}

  .offer-card{left:431px;top:119px;width:321px;height:183px;background:var(--white);border-radius:8px}
  .offer-img{left:7px;top:7px;width:163px;height:169px;border-radius:6px;background:linear-gradient(160deg,#3d7fd0 0%,#9fc3e6 45%,#b6404a 70%,#8b3a2a 100%)}
  .offer-title{left:187px;top:23px;font-size:13.6px;font-weight:500;line-height:17px;color:var(--orange)}
  .offer-sub{left:187px;top:69px;font-size:10px;font-weight:500;color:var(--ink)}
  .offer-body{left:189px;top:88px;width:122px;font-size:7.8px;line-height:13.7px;color:#444}
  .dot{width:10px;height:10px;border-radius:50%;display:flex;align-items:center;justify-content:center}
  .dot-prev{left:191px;top:156px;background:#dcdcdc}
  .dot-next{left:207px;top:156px;background:var(--orange)}

  .redeem-bar{left:105px;top:352px;width:641px;height:68px;background:var(--white);border-radius:10px;box-shadow:0 4px 16px rgba(0,0,0,.07)}
  .field{top:14px;height:39px;background:var(--field);border:1px solid var(--line);font-size:9.8px;color:#666;display:flex;align-items:center;padding-left:18px;letter-spacing:.2px}
  .field-id{left:16px;width:222px}
  .field-mail{left:253px;width:222px}
  .redeem-btn{left:488px;top:14px;width:132px;height:39px;background:var(--orange);color:var(--white);font-size:10.5px;font-weight:700;display:flex;align-items:center;padding-left:22px;gap:26px}

  /* welcome */
  .welcome-title{left:0;top:462px;width:853px;text-align:center;font-size:27px;font-weight:400;color:#4a4a4a}
  .welcome-title span{font-weight:700;color:var(--orange)}
  .welcome-copy{left:0;top:514px;width:853px;text-align:center;font-size:9.7px;line-height:20px;color:var(--text);font-weight:300}
  .welcome-copy strong{font-weight:500;color:var(--ink)}

  /* promo band */
  .promo{left:0;top:632px;width:853px;height:252px;background:var(--band)}
  .promo-photo{left:444px;top:0;width:409px;height:252px;background:linear-gradient(90deg,var(--band) 0%,#d8c8c0 35%,#c9a48c 60%,#d9cfc8 100%)}
  .promo-frame{left:143px;top:49px;width:140px;height:158px}
  .gift{left:101px;top:90px;width:82px;height:82px;border-radius:50%;background:var(--teal)}
  .promo-lead{left:201px;top:84px;font-family:'Poppins',sans-serif;font-size:10px;color:var(--ink)}
  .promo-title{left:201px;top:102px;font-family:'Poppins',sans-serif;font-weight:800;font-size:20.5px;line-height:27px;color:var(--orange)}
  .promo-sub{left:198px;top:158px;font-size:9.7px;color:var(--ink)}
  .promo-btn{left:175px;top:193px;width:84px;height:27px;background:var(--orange);color:var(--white);font-size:9.5px;font-weight:700;display:flex;align-items:center;justify-content:center}

  /* testimonials */
  .section-title{left:0;top:918px;width:853px;text-align:center;font-size:20.5px;font-weight:700;color:#444}
  .review{top:981px;width:198px;height:144px;background:#fafafa;border:1px solid #eeeeee;border-radius:8px}
  .quote{top:-10px;right:22px;font-family:'Poppins',sans-serif;font-weight:800;font-size:28px;line-height:28px;color:var(--orange);letter-spacing:-1px}
  .avatar{left:13px;top:16px;width:24px;height:24px;border-radius:50%;background:linear-gradient(135deg,#8a8f9a,#d9d4cf)}
  .who{left:44px;top:16px}
  .who b{display:block;font-size:11px;font-weight:500;color:#555}
  .who span{display:block;font-size:7.5px;color:#888;margin-top:2px}
  .review p{position:absolute;left:16px;top:55px;width:170px;font-size:8.6px;line-height:17px;color:var(--text);font-weight:300}

  .footer{left:0;top:1166px;width:853px;height:34px;background:var(--footer);font-size:8.2px;color:#666;display:flex;align-items:center;justify-content:center}
</style>
</head>
<body>

<svg class="abs hero-bg" viewBox="0 0 853 420" role="img" aria-label="Aerial photo of a red suspension bridge over a blue bay">
  <defs>
    <linearGradient id="heroGrad" x1="0" y1="0" x2="1" y2="1">
      <stop offset="0" stop-color="#3b3f86"/>
      <stop offset=".45" stop-color="#33548f"/>
      <stop offset="1" stop-color="#2a3e7c"/>
    </linearGradient>
  </defs>
  <path d="M0 0H853V364Q426 410 0 368Z" fill="url(#heroGrad)"/>
  <path d="M0 368Q426 410 853 364V420H0Z" fill="#ffffff"/>
</svg>

<div class="abs brand">
  <div class="brand-name"><span class="brand-dot"></span>BrightPerksPortal</div>
  <div class="brand-tag">Redemption Processing Center</div>
</div>

<nav class="abs nav" style="left:0;width:853px">
  <a style="left:488px">Home</a>
  <a style="left:547px">Contact us</a>
  <a style="left:627px">Testimonials</a>
  <a style="left:721px">Terms</a>
</nav>

<h1 class="abs hero-title">Welcome To The<br>Redemption Source</h1>
<p class="abs hero-text">Please Enter A Valid Certificate Id In The Form Below To Redeem Your Certificate And To View Faq's, Terms And Locations.</p>

<div class="abs offer-card">
  <div class="abs offer-img" role="img" aria-label="Photo of a red pagoda with a city and mountain behind"></div>
  <h2 class="abs offer-title">REDEEM SPECIAL<br>OFFERS</h2>
  <div class="abs offer-sub">Certificate Courtesy Of</div>
  <p class="abs offer-body">There is no doubt that Las Vegas is one of the hottest travel desti-nations around the world. travel destinations around the world.</p>
  <span class="abs dot dot-prev"><svg width="4" height="5" viewBox="0 0 4 5"><path d="M3 .5 1 2.5 3 4.5" fill="none" stroke="#777" stroke-width=".8"/></svg></span>
  <span class="abs dot dot-next"><svg width="4" height="5" viewBox="0 0 4 5"><path d="M1 .5 3 2.5 1 4.5" fill="none" stroke="#fff" stroke-width=".8"/></svg></span>
</div>

<form class="abs redeem-bar">
  <div class="abs field field-id">ENTER YOUR CERTIFICATE ID #</div>
  <div class="abs field field-mail">ENTER YOUR EMAIL</div>
  <div class="abs redeem-btn">REDEEM
    <svg width="16" height="16" viewBox="0 0 16 16"><path d="M15 1 1 7l5 2 2 6 7-14ZM6 9l9-8M8 15l-1-4" fill="none" stroke="#fff" stroke-width=".9" stroke-linejoin="round"/></svg>
  </div>
</form>

<h2 class="abs welcome-title">WELCOME <span>BRIGHTPERKSPORTAL</span></h2>
<div class="abs welcome-copy">
  BrightPerksPortal.net is a leading company in travel certificate fulfillment.<br>
  Our goal is to make it easy for you to redeem your certificate and our philosophy is this:<br>
  <strong>"What good is it to receive a gift certificate if you can't use it?".</strong><br>
  If you have any questions about how to redeem a certificate, please contact us. We are here to help
</div>

<section class="abs promo">
  <div class="abs promo-photo" role="img" aria-label="Photo of two friends on a sofa looking at a phone"></div>
  <svg class="abs promo-frame" viewBox="0 0 140 158">
    <path d="M2 30V2H138V28M138 138V156H117M49 156H2V128" fill="none" stroke="#5ec3cf" stroke-width="2.5"/>
  </svg>
  <div class="abs gift" role="img" aria-label="Gift box illustration"></div>
  <div class="abs promo-lead">Please Enter a</div>
  <div class="abs promo-title">VALID CERTIFICATE<br>ID NUMBER</div>
  <div class="abs promo-sub">to view the deals and to redeem and active your special offer</div>
  <div class="abs promo-btn">View Now</div>
</section>

<h2 class="abs section-title">TESTIMONIALS</h2>

<article class="abs review" style="left:111px">
  <span class="abs quote">99</span>
  <div class="abs avatar" role="img" aria-label="Customer portrait"></div>
  <div class="abs who"><b>Marlon T.</b><span>Duluth, GA</span></div>
  <p>I worked with the travel agency and they were very patient with me as I narrowed down where myself and another friend wanted to travel to.</p>
</article>
<article class="abs review" style="left:328px">
  <span class="abs quote">99</span>
  <div class="abs avatar" role="img" aria-label="Customer portrait"></div>
  <div class="abs who"><b>Rowena K.</b><span>North Las Vegas, NV</span></div>
  <p>The travel agency did an excellent job booking my trip to Nashville.</p>
</article>
<article class="abs review" style="left:543px">
  <span class="abs quote">99</span>
  <div class="abs avatar" role="img" aria-label="Customer portrait"></div>
  <div class="abs who"><b>Elias V.</b><span>Flagstaff, AZ</span></div>
  <p>Wonderful! It was just like being in Rome, but only with great shows to enjoy. The rooms of the Solano Grand and service were excellent.</p>
</article>

<footer class="abs footer">Copyright © 2013-2020 Northwind Studio Co. All rights reserved.</footer>

</body>
</html>
```